Home page graphic design only (NOT WEBSITE DESIGN)

I require a home page to be designed for my new website.
I DO NOT REQUIRE to build a website. We are a rug company specialising in alpaca wool. It is targeted at the high end of the market and hence the graphics of our page requires to reflect this. Our current page is as per attachment and I think it is too basic.
Updates

Target Market(s)

Extremly high net worth individuals where luxury is a requirement

Requirements
Must have
• show of style, luxury, uniqueness. Prefer having bright images.
Nice to have
• a highly sofisticated roomscape where the focus in the rug. See attachment as an example
Should not have
• Not sure

```html
<!DOCTYPE html>
<html lang="en">
<head>
<meta charset="utf-8">
<title>Maison Lumière – Home</title>
<link rel="stylesheet" href="https://fonts.googleapis.com/css2?family=Marcellus&family=Cinzel:wght@400;500&family=Arimo&display=swap">
<style>
  :root {
    --page-bg: #ffffff;
    --header-bg: #0a0a0a;
    --black: #000000;
    --navy-top: #07080c;
    --navy-bottom: #121521;
    --gold: #d4a24c;
    --gold-light: #f3dc8a;
    --gold-deep: #a8733a;
    --nav-text: #f2f2f2;
    --footer-text: #bdbdbd;
    --icon-grey: #8c8c8c;
    --rule: #3a2f1c;
  }
  * { margin: 0; padding: 0; box-sizing: border-box; }
  html, body { width: 1200px; height: 1200px; overflow: hidden; background: var(--page-bg); }
  .home {
    position: absolute; left: 36px; top: 270px;
    width: 1127px; height: 660px;
    background: var(--black); overflow: hidden;
  }
  .site-header {
    position: absolute; left: 0; top: 0; width: 100%; height: 52px;
    background: var(--header-bg);
  }
  .site-header::after {
    content: ""; position: absolute; left: 15px; top: 52px;
    width: 864px; height: 1px; background: var(--rule);
  }
  .brand {
    position: absolute; left: 38px; top: 13px;
    font-family: "Marcellus", serif; font-size: 24px; color: var(--gold);
    letter-spacing: 0.5px;
  }
  .main-nav a {
    position: absolute; top: 10px;
    font-family: "Arimo", sans-serif; font-size: 11.5px; color: var(--nav-text);
    text-decoration: none; white-space: nowrap;
  }
  .main-nav a.is-active { color: var(--gold); }
  .main-nav .caret {
    position: absolute; left: 386px; top: 16px;
    border-left: 3px solid transparent; border-right: 3px solid transparent;
    border-top: 4px solid var(--nav-text);
  }
  .header-mark {
    position: absolute; left: 1070px; top: 14px; width: 24px; height: 24px;
    border-radius: 50%; border: 2px solid var(--gold);
  }
  .stage { position: absolute; left: 0; top: 0; width: 1127px; height: 660px; }
  .emblem-art {
    position: absolute; left: 748px; top: 78px; width: 350px; height: 496px;
    background: radial-gradient(ellipse at 55% 60%, rgba(228,184,96,0.35) 0%, rgba(168,115,58,0.15) 45%, rgba(0,0,0,0) 72%);
  }
  .hero-text {
    position: absolute; left: 43px; top: 170px; width: 600px;
    text-align: center; color: var(--gold);
  }
  .flourish {
    display: block; margin: 0 auto; width: 62px; height: 22px; border-radius: 11px;
    background: linear-gradient(90deg, var(--gold-deep), var(--gold-light), var(--gold));
    opacity: 0.55;
  }
  .hero-title {
    margin-top: 36px;
    font-family: "Marcellus", serif; font-weight: 400; font-size: 33px;
    color: var(--gold); letter-spacing: 1px; line-height: 1;
  }
  .tagline {
    margin-top: 18px;
    font-family: "Cinzel", serif; font-size: 16px; line-height: 21px;
    letter-spacing: 0.6px; color: var(--gold);
  }
  .divider {
    position: relative; margin: 31px auto 0; width: 152px; height: 10px;
  }
  .divider::before {
    content: ""; position: absolute; left: 0; top: 4px; width: 100%; height: 2px;
    background: linear-gradient(90deg, rgba(212,162,76,0), var(--gold) 30%, var(--gold-light) 50%, var(--gold) 70%, rgba(212,162,76,0));
  }
  .divider .divider-knot {
    position: absolute; left: 52px; top: 1px; width: 48px; height: 8px; border-radius: 4px;
    background: var(--gold); opacity: 0.8;
  }
  .company-info {
    margin-top: 20px;
    font-family: "Cinzel", serif; font-size: 13.5px; line-height: 16px;
    letter-spacing: 0.4px; color: var(--gold);
  }
  .hero-text .flourish.bottom { margin-top: 54px; }
  .site-footer {
    position: absolute; left: 0; top: 622px; width: 100%; height: 38px;
  }
  .site-footer::before {
    content: ""; position: absolute; left: 15px; top: 0; width: 533px; height: 1px;
    background: #2a2a2a;
  }
  .copyright {
    position: absolute; left: 28px; top: 14px;
    font-family: "Arimo", sans-serif; font-size: 8.8px; color: var(--footer-text);
    white-space: nowrap;
  }
  .social { position: absolute; left: 973px; top: 10px; display: flex; gap: 9px; }
  .social span {
    width: 18px; height: 18px; border-radius: 50%; background: var(--icon-grey);
  }
</style>
</head>
<body>
<div class="home">
  <svg class="stage" viewBox="0 0 1127 660" aria-hidden="true">
    <defs>
      <linearGradient id="navy-fill" x1="0" y1="0" x2="0" y2="1">
        <stop offset="0" stop-color="#07080c"/>
        <stop offset="1" stop-color="#121521"/>
      </linearGradient>
      <linearGradient id="gold-sweep" x1="0" y1="0" x2="0" y2="1">
        <stop offset="0" stop-color="#f3dc8a"/>
        <stop offset="0.5" stop-color="#e6b860"/>
        <stop offset="1" stop-color="#a8733a"/>
      </linearGradient>
    </defs>
    <path d="M0 52 L870 52 C790 130 760 300 722 420 C684 530 612 600 548 622 L0 622 Z" fill="url(#navy-fill)"/>
    <path d="M870 52 C790 130 760 300 722 420 C684 530 612 600 548 622" fill="none" stroke="url(#gold-sweep)" stroke-width="3.5" stroke-linecap="round"/>
  </svg>

  <div class="emblem-art" role="img" aria-label="Large gold brand emblem artwork"></div>

  <header class="site-header">
    <div class="brand">Maison Lumière</div>
    <nav class="main-nav">
      <a class="is-active" href="#" style="left:235px">Home</a>
      <a href="#" style="left:302px">Collections</a>
      <span class="caret"></span>
      <a href="#" style="left:396px">Our Story</a>
      <a href="#" style="left:479px">About us</a>
      <a href="#" style="left:562px">FAQ</a>
      <a href="#" style="left:622px">Publications</a>
      <a href="#" style="left:721px">News &amp; Events</a>
      <a href="#" style="left:836px">Contact us</a>
    </nav>
    <span class="header-mark"></span>
  </header>

  <section class="hero-text">
    <span class="flourish" role="img" aria-label="Gold scroll flourish ornament"></span>
    <h1 class="hero-title">Maison Lumière</h1>
    <p class="tagline">Exquisite luxury carpenting and area rugs made<br>from pure&nbsp; Peruvian alpaca</p>
    <div class="divider"><span class="divider-knot" role="img" aria-label="Gold knot ornament"></span></div>
    <p class="company-info">
      Estabilished in 1988<br>
      AUSTRALIA - USA - EUROPE - UK ASIA - UAE<br>
      Maison Lumière Pty Ltd<br>
      ABN 12 345 678 901
    </p>
    <span class="flourish bottom" role="img" aria-label="Gold scroll flourish ornament"></span>
  </section>

  <footer class="site-footer">
    <p class="copyright">Copyright @2020 Maison Lumière - Australia - Head Office - Suite 5 / Unit 120 – 88 Willow Bank Road;Willow Bank VIC 3999</p>
    <div class="social" aria-label="Social links">
      <span></span><span></span><span></span><span></span><span></span>
    </div>
  </footer>
</div>
</body>
</html>
```